PlumEcho Social Sharing Platform Needs a Redesign (2 pages / Design only)

PlumEcho is a popular social sharing platform for bloggers and marketers. The site has been quite popular for a few years now, but the site's design is looking quite dated. We're looking for a brand new design to give the service a facelift.

We are looking for a modern and fresh design that keeps all the existing functionality intact. Would prefer designs that incorporate the color blue in them.

We would like the two attached screenshots to be redesigned and submitted - using he same content. Please do not submit a redesign of the front page (non-logged in version). Redesign the 2 attached pages only, and the final deliverable is these two pages as layered PSD files.

Target Market(s)

bloggers, internet marketers

Industry/Entity Type

Social

Number of Pages Required

2 page

Requirements
Must have
• All existing functionality must be intact as seen from the screenshots.
Should not have
• Please do not submit designs based on existing front page (non-logged in version). Use attached screenshots (file 1 and 2) as a guide of existing functionality.

```html
<!DOCTYPE html>
<html lang="en">
<head>
<meta charset="utf-8">
<title>PlumEcho – Submit a Post</title>
<link rel="stylesheet" href="https://fonts.googleapis.com/css2?family=Sorts+Mill+Goudy&family=Noto+Sans:wght@400;700&display=swap">
<style>
:root{
  --blue:#3a78ad;
  --blue-dark:#2f6796;
  --ink:#222;
  --muted:#444;
  --green:#4caf50;
  --link:#2a6fb8;
  --red:#d9302b;
  --line:#b9b9b9;
  --white:#fff;
  --shot-a:#c9d7e6;
  --shot-b:#e8edf2;
}
*{box-sizing:border-box;margin:0;padding:0}
html,body{width:1200px;height:900px;overflow:hidden;background:var(--white)}
body{position:relative;font-family:"Noto Sans",sans-serif;color:var(--ink)}

.brand{position:absolute;left:30px;top:28px;display:flex;align-items:center;gap:10px}
.brand-mark{width:32px;height:32px;background:var(--blue)}
.brand-name{font-family:"Sorts Mill Goudy",serif;font-size:36px;line-height:1;color:var(--ink);letter-spacing:1px}

.account{position:absolute;right:38px;top:28px;text-align:right;font-family:"Sorts Mill Goudy",serif;color:var(--blue-dark);font-size:12px}
.account .logout{display:flex;justify-content:flex-end;align-items:center;gap:10px;font-size:13px;margin-bottom:8px}

.nav{position:absolute;left:12px;top:98px;width:1190px;height:52px}
.nav-item{position:absolute;top:0;width:152px;height:52px}
.nav-item svg{position:absolute;inset:0}
.nav-item span{position:absolute;left:0;right:16px;top:0;bottom:0;display:flex;align-items:center;justify-content:center;text-align:center;color:var(--white);font-family:"Sorts Mill Goudy",serif;font-size:12px;line-height:1.25}

.panel{position:absolute;border:3px solid var(--blue);border-radius:10px;background:var(--white)}
.submit-panel{left:56px;top:193px;width:677px;height:508px}
.row{position:absolute;left:33px;font-size:10px;line-height:12px;color:var(--muted);white-space:nowrap}
.panel-title{font-family:"Sorts Mill Goudy",serif;font-size:19px;line-height:22px;font-weight:400;color:var(--blue-dark);border-bottom:1px solid var(--blue);letter-spacing:.5px}
.notice{font-style:italic;white-space:normal;width:600px}
.input{position:absolute;left:33px;border:1px solid #bbb;height:16px;width:178px;font-size:9.5px;line-height:14px;padding:0 4px;color:var(--ink)}
.textarea{width:566px;height:28px}
.hint{position:absolute;left:215px;font-size:10px;line-height:16px;color:var(--green)}
.num{color:var(--green)}
.check{display:flex;align-items:center;gap:6px}
.box{width:11px;height:11px;border:1px solid #999;border-radius:2px;display:inline-block;position:relative}
.select{position:absolute;left:33px;width:171px;height:12px;border:1px solid #999;border-radius:2px;font-size:8.5px;line-height:10px;padding:0 6px;display:flex;justify-content:space-between;font-weight:700;color:var(--ink)}
.btn{position:absolute;left:33px;width:110px;height:24px;background:var(--blue);color:var(--white);font-family:"Sorts Mill Goudy",serif;font-size:11px;line-height:24px;text-align:center;border-radius:12px}
.footnote a{color:var(--link);text-decoration:underline}

.bar{position:absolute;background:var(--blue);color:var(--white);font-family:"Sorts Mill Goudy",serif;border-radius:12px;display:flex;align-items:center}
.posted-bar{left:56px;top:714px;width:675px;height:23px;font-size:14px}
.posted-bar .l{margin-left:125px}
.posted-bar .r{margin-left:auto;margin-right:52px}

.tweets{position:absolute;left:64px;top:748px;width:664px}
.tweet{border-bottom:1px solid var(--line);padding:4px 4px 6px;position:relative;font-size:9.5px;line-height:1.35}
.tweet .meta{color:var(--muted)}
.tweet .text a{color:var(--ink);text-decoration:underline}
.tweet .stats{margin-top:2px;display:flex;gap:16px}
.tweet .stats .rt,.tweet .stats .lk{color:var(--link)}
.tweet .stats .po{color:var(--red)}
.tweet .actions{position:absolute;right:12px;top:4px;display:flex;gap:10px}

.credits{position:absolute;left:789px;top:204px;width:363px;height:126px;background:var(--blue);border-radius:10px;color:var(--white);font-family:"Sorts Mill Goudy",serif;text-align:center;font-size:17px;line-height:26px;padding-top:8px}
.credits .amount{font-size:23px;font-weight:700;font-variant-numeric:lining-nums}
.featured-bar{left:789px;top:363px;width:363px;height:37px;justify-content:center;font-size:14px;border-radius:8px}

.featured{left:786px;top:427px;width:364px;height:405px;padding:32px 28px}
.site-title{font-size:13px;font-weight:700;text-decoration:underline;line-height:1.05;letter-spacing:.3px}
.shot{border:1px solid #aaa;background:linear-gradient(180deg,var(--shot-a),var(--shot-b))}
.site-desc{font-size:11px;line-height:1.3;color:var(--ink);margin-top:4px;letter-spacing:.3px}
</style>
</head>
<body>

<div class="brand"><span class="brand-mark"></span><span class="brand-name">PLUMECHO</span></div>

<div class="account">
  <div class="logout">LOG OUT
    <svg width="18" height="20" viewBox="0 0 18 20"><circle cx="9" cy="5.5" r="5" fill="#3a78ad"/><path d="M0 20 Q0 11 9 11 Q18 11 18 20Z" fill="#3a78ad"/></svg>
  </div>
  <div>WELCOME MR PLUMECHO</div>
</div>

<nav class="nav">
  <div class="nav-item" style="left:0"><svg width="152" height="52"><polygon points="0,0 128,0 152,26 128,52 0,52 18,26" fill="#3a78ad"/></svg><span>DASHBOARD</span></div>
  <div class="nav-item" style="left:171px"><svg width="152" height="52"><polygon points="0,0 128,0 152,26 128,52 0,52 18,26" fill="#3a78ad"/></svg><span>CHIRPLINE<br>FOLLOWERS</span></div>
  <div class="nav-item" style="left:342px"><svg width="152" height="52"><polygon points="0,0 128,0 152,26 128,52 0,52 18,26" fill="#3a78ad"/></svg><span>SUBMIT<br>POST</span></div>
  <div class="nav-item" style="left:513px"><svg width="152" height="52"><polygon points="0,0 128,0 152,26 128,52 0,52 18,26" fill="#3a78ad"/></svg><span>ACTIVITY<br>SUMMARY</span></div>
  <div class="nav-item" style="left:684px"><svg width="152" height="52"><polygon points="0,0 128,0 152,26 128,52 0,52 18,26" fill="#3a78ad"/></svg><span>BUY<br>CREDITS</span></div>
  <div class="nav-item" style="left:855px"><svg width="152" height="52"><polygon points="0,0 128,0 152,26 128,52 0,52 18,26" fill="#3a78ad"/></svg><span>SETTINGS</span></div>
  <div class="nav-item" style="left:1026px"><svg width="152" height="52"><polygon points="0,0 128,0 152,26 128,52 0,52 18,26" fill="#3a78ad"/></svg><span>AFFILIATES</span></div>
</nav>

<section class="panel submit-panel">
  <h1 class="row panel-title" style="top:14px">SUBMIT A POST</h1>
  <p class="row notice" style="top:58px">Please do not request reposts for sales pages, direct affiliate links, squeeze pages, homepage links, and other overly promotional or low quality content. These will be deleted.</p>

  <div class="row" style="top:96px">Post ( <b>RT @plum_hollis</b> will be added automatically to your message )</div>
  <div class="input textarea" style="top:111px"></div>
  <div class="row" style="top:142px">(You have <span class="num">124</span> characters left)</div>

  <div class="row" style="top:168px">How many credits would you like to offer members to promote this message</div>
  <div class="input" style="top:182px"></div>

  <div class="row" style="top:214px">Maximum times to promote</div>
  <div class="input" style="top:228px">0</div>
  <div class="hint" style="top:228px">You will spend <b>0</b> credits</div>

  <div class="row" style="top:261px">Select which Social Networks to allow</div>
  <div class="row check" style="top:276px"><span class="box"><svg width="9" height="9" style="position:absolute;left:0;top:0"><path d="M1.5 4.5 L3.5 6.5 L7.5 2" stroke="#999" fill="none" stroke-width="1.2"/></svg></span>Chirpline</div>
  <div class="row check" style="top:290px"><span class="box"></span>Friendspace</div>
  <div class="row check" style="top:304px"><span class="box"></span>Circles+</div>

  <div class="row" style="top:334px">Minimum number of Chirpline followers to promote</div>
  <div class="input" style="top:347px">0</div>
  <div class="hint" style="top:347px"><b>100%</b> of members will see this post.</div>

  <div class="row" style="top:379px">Category</div>
  <div class="select" style="top:394px">Please Select <span>&#9662;</span></div>

  <div class="btn" style="top:419px">SUBMIT</div>

  <p class="row footnote" style="top:454px">This submitted post <b>will be posted immediately</b> to your Chirpline<br>timeline. You can change this option by going to the <a>Settings page</a>.</p>
</section>

<div class="bar posted-bar"><span class="l">POSTED POSTS</span><span class="r">ACTIONS</span></div>

<div class="tweets">
  <div class="tweet">
    <div class="meta">Posted 421 days ago for 35 credits (Completed)</div>
    <div class="text">Top Affiliate Marketing Blogs and News Feeds <a>http://marawinslow.com/top-affiliate-marketing-blogs-news-feeds/</a></div>
    <div class="stats"><span class="rt">Reposts (17)</span><span class="lk">Likes (10)</span><span class="po">PlusOnes (8)</span></div>
    <div class="actions">
      <svg width="12" height="12"><path d="M2 10 L9 3 L10.5 4.5 L3.5 11.5 L1.5 11.5Z" fill="#e0a52a"/></svg>
      <svg width="12" height="12"><circle cx="6" cy="6" r="5.5" fill="#4caf50"/><path d="M3 6H9M6 3V9" stroke="#fff" stroke-width="1.6"/></svg>
      <svg width="12" height="12"><path d="M2 2L10 10M10 2L2 10" stroke="#d9302b" stroke-width="2.2"/></svg>
    </div>
  </div>
  <div class="tweet">
    <div class="meta">Posted 476 days ago for 30 credits (Completed)</div>
    <div class="text">Introducing Blogwatch Hub: The New Way To Get Your Marketing News<br><a>http://plumhollis.com/introducing-blogwatch-hub</a></div>
    <div class="stats"><span class="rt">Reposts (29)</span><span class="lk">Likes (10)</span><span class="po">PlusOnes (11)</span></div>
    <div class="actions">
      <svg width="12" height="12"><path d="M2 10 L9 3 L10.5 4.5 L3.5 11.5 L1.5 11.5Z" fill="#e0a52a"/></svg>
      <svg width="12" height="12"><circle cx="6" cy="6" r="5.5" fill="#4caf50"/><path d="M3 6H9M6 3V9" stroke="#fff" stroke-width="1.6"/></svg>
      <svg width="12" height="12"><path d="M2 2L10 10M10 2L2 10" stroke="#d9302b" stroke-width="2.2"/></svg>
    </div>
  </div>
</div>

<aside class="credits">
  <div>YOU HAVE</div>
  <div class="amount">390059</div>
  <div>CREDITS LEFT</div>
  <div>REPOST NOW</div>
</aside>

<div class="bar featured-bar">FEATURED WEBSITES</div>

<section class="panel featured">
  <div class="site-title">Online Business Marketing<br>Success with Nora Lindqvist</div>
  <div class="shot" role="img" aria-label="Screenshot of the Nora Lindqvist marketing blog homepage" style="width:250px;height:110px;margin-top:3px"></div>
  <div class="site-desc">Have fun and learn about making more<br>money online.</div>
  <div class="site-title" style="margin-top:18px">BrightVentureNotes</div>
  <div class="shot" role="img" aria-label="Screenshot of the BrightVentureNotes business news site" style="width:284px;height:113px;margin-top:3px"></div>
  <div class="site-desc">Your daily dose of smart business news and<br>trends!</div>
</section>

</body>
</html>
```